Flyer to promote new Commercial HVAC Preventative Maintenance clients

This flyer will be in the body of emails that will be sent to new, existing, and/or potential commericial buildings HVAC clients. It will have the least amount of words used, but it will convey the point with pertinent pictorial and graphics. It will show the value of a Periodic/Preventative routine maintenance to lower operating costs of their commericial buildings (i.e. office, medical, shopping centers, apartment, warehouse facility, etc.), in the following ways:
1) Reduce monthly power usage,
2) Reduce emergency HVAC service calls,
3) Reduce costly repairs costs,
4) Reduce HVAC down-times and angry tenants,
5) Increases the life expectancy of the existing and/or new HVAC equipment in the building and/or the equipment's' early replacement costs,
6) Reduces tenant's early termination of their lease and law suits against the landlords,
7) Increases tenant's renewal of the lease and agree to pay the increase rental rates,
8) Reduces unhappy customers and increases tenant's productivity,
9) By reducing the landlord's expenses, the value of the property will increase considerably and profitable to sell their holdings, or refinance and keep their holdings with an increased ROI (Return On Investment).

Landlords can not depend on their tenants' obligation to maintain the landlords' major assets, which is their HVAC equipment and systems.

With the periodic maintenance done by one reliable and licensed HVAC company, the will not use different companies that may or may not do the right repair job on their unit and hurt their bottom line and increase HVAC replacement COSTLY rates.

```html
<!DOCTYPE html>
<html lang="en">
<head>
<meta charset="utf-8">
<title>Routine HVAC Maintenance Flyer</title>
<link href="https://fonts.googleapis.com/css2?family=Poppins:wght@500;600;700&display=swap" rel="stylesheet">
<style>
:root{
  --navy:#124f7a;
  --blue:#1565c0;
  --bar:#1a2f8f;
  --grey:#6b6b6b;
  --ink:#1b1b1b;
  --tile-light:#d7eaf9;
  --tile-mid:#a9d5f6;
  --note-blue:#1a5a8c;
  --accent:#70baf1;
  --white:#ffffff;
}
*{box-sizing:border-box;margin:0;padding:0}
html,body{width:669px;height:1200px;overflow:hidden;background:var(--white)}
body{font-family:"Poppins",sans-serif;color:var(--ink);position:relative}
.flyer{position:absolute;left:79px;top:105px;width:502px;height:973px;background:var(--white)}
.abs{position:absolute}
.hero-art{left:21px;top:23px;width:130px;height:122px;border-radius:10px;
  background:linear-gradient(160deg,#e9ecef,#b9c2ca)}
.title{left:170px;top:50px;width:320px;white-space:nowrap}
.title .kicker{font-size:14.5px;font-weight:600;color:var(--grey);line-height:18px}
.title .headline{font-size:23.5px;font-weight:700;color:var(--blue);line-height:30px}
.title .sub{margin-top:2px;border-left:4px solid var(--bar);padding-left:6px;font-size:17.5px;font-weight:500;line-height:21px}
.sectors{left:0;top:149px;width:502px;height:104px;background:var(--navy);display:flex;padding:14px 8px 0}
.sector{flex:1;text-align:center;color:var(--white);font-size:13px;font-weight:600;line-height:15.6px;position:relative}
.sector+.sector::before{content:"";position:absolute;left:0;top:0;height:54px;border-left:1px dashed rgba(255,255,255,.8)}
.sector .ring{width:38px;height:38px;margin:0 auto 8px;border-radius:50%;background:var(--white);border:2px solid #7fb9e6;display:flex;align-items:center;justify-content:center}
.sector svg{width:22px;height:22px}
.tile{border-radius:7px;font-size:12.5px;font-weight:500;line-height:15.6px;white-space:nowrap}
.light{background:var(--tile-light)}
.mid{background:var(--tile-mid)}
.tile .text{position:absolute}
.icon-slot{position:absolute;border-radius:6px;background:linear-gradient(135deg,#f2c94c,#e57373 60%,#4fb3c9)}
.wide .text{left:9px;top:9px;font-size:12.5px}
.wide .icon-slot{right:22px;top:6px;width:40px;height:38px}
.note{left:20px;top:766px;width:462px;text-align:center;font-size:14.5px;font-weight:500;line-height:17.5px;white-space:nowrap}
.note strong{color:var(--note-blue);font-weight:700}
.closing{left:0;top:828px;width:502px;height:145px;background:var(--navy);color:var(--white);text-align:center;font-size:14.5px;font-weight:600;line-height:17.5px;padding-top:12px;white-space:nowrap}
.closing .punch{display:block;color:var(--accent);font-size:18px;font-weight:700;line-height:22px;margin-top:2px}
</style>
</head>
<body>
<main class="flyer">
  <div class="abs hero-art" role="img" aria-label="Illustration of technicians servicing a rooftop HVAC chiller unit"></div>
  <header class="abs title">
    <p class="kicker">VALUE OF A PERIODIC/PREVENTATIVE</p>
    <h1 class="headline">ROUTINE MAINTENANCE</h1>
    <p class="sub">to lower operating costs of their<br>commercial buildings</p>
  </header>

  <section class="abs sectors">
    <div class="sector"><div class="ring"><svg viewBox="0 0 24 24" fill="none" stroke="#124f7a" stroke-width="2"><rect x="3" y="12" width="18" height="3"/><path d="M6 15v6M18 15v6M9 12V6h8v6"/></svg></div>Office</div>
    <div class="sector"><div class="ring"><svg viewBox="0 0 24 24"><circle cx="12" cy="12" r="11" fill="#124f7a"/><path d="M10 5h4v5h5v4h-5v5h-4v-5H5v-4h5z" fill="#fff"/></svg></div>Medical</div>
    <div class="sector"><div class="ring"><svg viewBox="0 0 24 24" fill="none" stroke="#124f7a" stroke-width="2"><path d="M2 4h3l3 11h11l2-8H6"/><circle cx="9" cy="19" r="1.5"/><circle cx="17" cy="19" r="1.5"/></svg></div>Shopping<br>centers</div>
    <div class="sector"><div class="ring"><svg viewBox="0 0 24 24" fill="#124f7a"><rect x="4" y="8" width="7" height="14"/><rect x="12" y="3" width="8" height="19"/><path d="M14 6h1v2h-1zM17 6h1v2h-1zM14 10h1v2h-1zM17 10h1v2h-1z" fill="#fff"/></svg></div>Apartment</div>
    <div class="sector"><div class="ring"><svg viewBox="0 0 24 24" fill="#124f7a"><path d="M2 10L12 3l10 7v11H2z"/><path d="M7 12h10v2H7zM7 15h10v2H7zM7 18h10v2H7z" fill="#fff"/></svg></div>Warehouse<br>facility</div>
  </section>

  <div class="abs tile light" style="left:40px;top:261px;width:126px;height:65px">
    <span class="text" style="left:8px;top:9px">Reduce<br>monthly<br>power usage.</span>
    <span class="icon-slot" role="img" aria-label="Light bulb and plug icon" style="right:7px;top:8px;width:31px;height:31px"></span>
  </div>
  <div class="abs tile mid" style="left:181px;top:261px;width:133px;height:75px">
    <span class="text" style="left:7px;top:7px">Reduce<br>emergency<br>HVAC<br>service calls.</span>
    <span class="icon-slot" role="img" aria-label="Support agent icon" style="right:5px;top:10px;width:36px;height:37px"></span>
  </div>
  <div class="abs tile light" style="left:322px;top:261px;width:133px;height:75px">
    <span class="text" style="left:10px;top:14px">Reduce<br>costly<br>repairs costs</span>
    <span class="icon-slot" role="img" aria-label="Repair tools icon" style="right:10px;top:10px;width:36px;height:36px"></span>
  </div>

  <div class="abs tile mid" style="left:40px;top:337px;width:126px;height:106px">
    <span class="text" style="left:8px;top:27px">Reduce<br>HVAC<br>down-times<br>&amp; angry tenants</span>
    <span class="icon-slot" role="img" aria-label="Clock with down arrow icon" style="left:72px;top:17px;width:40px;height:40px;border-radius:50%"></span>
  </div>
  <div class="abs tile light" style="left:179px;top:343px;width:259px;height:100px">
    <span class="text" style="left:10px;top:9px">Increases the life expectancy of the<br>existing and/or new HVAC<br>equipment in the building<br>and/or the equipment's'<br>early replacement costs.</span>
    <span class="icon-slot" role="img" aria-label="Cost path to replacement unit icon" style="right:9px;top:30px;width:52px;height:54px"></span>
  </div>

  <div class="abs tile light wide" style="left:40px;top:459px;width:424px;height:51px"><span class="text">Reduces tenant's early termination of their lease<br>and law suits against the landlords.</span><span class="icon-slot" role="img" aria-label="House with security badge icon"></span></div>
  <div class="abs tile mid wide" style="left:40px;top:523px;width:424px;height:51px"><span class="text">Increases tenant's renewal of the lease and agree<br>to pay the increase rental rates</span><span class="icon-slot" role="img" aria-label="Rising rent house icon" style="border-radius:50%"></span></div>
  <div class="abs tile light wide" style="left:40px;top:586px;width:424px;height:51px"><span class="text">Reduces unhappy customers and increases<br>tenant's productivity</span><span class="icon-slot" role="img" aria-label="Satisfaction gauge icon"></span></div>
  <div class="abs tile mid" style="left:40px;top:649px;width:424px;height:99px">
    <span class="icon-slot" role="img" aria-label="House with rising value chart icon" style="left:8px;top:21px;width:58px;height:56px"></span>
    <span class="text" style="left:76px;top:10px">By reducing the landlord's expenses, the value of<br>the property will increase considerably and<br>profitable to sell their holdings, or refinance and<br>keep their holdings with an increased ROI (Return<br>On Investment).</span>
  </div>

  <p class="abs note"><strong>Landlords can not depend on their tenants' obligation</strong><br>to maintain the landlords' major assets, which is their<br>HVAC equipment and systems.</p>

  <footer class="abs closing">With the periodic maintenance done by one reliable and<br>licensed HVAC company, the will not use different<br>companies that may or may not do the right repair job<br>on their unit and hurt their bottom line and<span class="punch">Increase HVAC replacement COSTLY rates.</span></footer>
</main>
</body>
</html>
```